Quiet Falcon Coffee

We need a website to sell coffee with a horse theme. We already have a logo and have designed 4 different coffee bags/flavors so far, each of which will be available in ground or whole bean. The brand is intended to be light hearted/whimsical.

Coding

Coded - Design and coding required

Number of Pages Required

4 page

Requirements
Must have
• incorporation of attached photos
Nice to have
• underlying background theme with sky/grass

```html
<!DOCTYPE html>
<html lang="en">
<head>
<meta charset="utf-8">
<title>Quiet Falcon Coffee</title>
<link href="https://fonts.googleapis.com/css2?family=Poppins:ital,wght@0,400;0,500;0,600;0,700;1,400&family=Open+Sans:wght@400;600&display=swap" rel="stylesheet">
<style>
:root{
  --espresso:#3a1812;
  --roast:#4a1f17;
  --maroon:#4a0d0d;
  --cream:#efe9e2;
  --sand:#f0c896;
  --tan:#e7c590;
  --caramel:#c9a26b;
  --rust:#7a2e12;
  --ink:#1c1412;
  --grey:#5d5856;
  --white:#ffffff;
}
*{margin:0;padding:0;box-sizing:border-box}
html,body{width:1200px;height:3859px;overflow:hidden}
body{position:relative;background:var(--cream);font-family:"Open Sans",sans-serif;color:var(--ink)}
.abs{position:absolute}
.backdrop{position:absolute;left:0;top:0;width:1200px;height:3859px}
.nav a{position:absolute;top:41px;font-family:"Poppins",sans-serif;font-size:16px;font-weight:500;color:var(--white);text-decoration:none}
.nav a.active{color:var(--sand)}
.pill{position:absolute;display:flex;align-items:center;justify-content:center;border-radius:40px;font-family:"Poppins",sans-serif;font-weight:500;text-decoration:none}
.btn-sand{background:var(--sand);color:var(--white)}
.btn-dark{background:var(--maroon);color:var(--white)}
.logo-disc{position:absolute;left:495px;top:-55px;width:210px;height:210px;border-radius:50%;background:var(--white);display:flex;flex-direction:column;align-items:center;justify-content:flex-end;padding-bottom:38px}
.brand-word{font-family:"Poppins",sans-serif;font-weight:600;color:var(--espresso);text-align:center;line-height:1.1}
.art{position:absolute}
.hero-kicker{left:114px;top:190px;font-family:"Poppins",sans-serif;font-size:36px;color:var(--sand);font-weight:400}
.hero-title{left:110px;top:236px;font-family:"Poppins",sans-serif;font-size:74px;line-height:86px;font-weight:600;color:var(--sand)}
.about-label{left:670px;top:694px;font-family:"Poppins",sans-serif;font-size:37px;font-weight:600;color:var(--white)}
.about-sub{left:670px;top:740px;font-family:"Poppins",sans-serif;font-size:34px;color:var(--white)}
.about-text{left:671px;top:804px;width:430px;font-size:15px;line-height:25px;color:var(--white)}
.purpose-card{left:93px;top:1304px;width:799px;height:466px;border-radius:0 0 60px 60px;border:7px solid var(--tan);border-top:none;border-right:none;overflow:hidden}
.purpose-card .photo{position:absolute;inset:0;background:linear-gradient(180deg,#f4f1ee 0%,#ece6df 55%,#d9cfc4 100%)}
.purpose-title{left:128px;top:1350px;width:640px;font-family:"Poppins",sans-serif;font-size:39px;line-height:53px;font-weight:600;color:var(--ink)}
.purpose-text{left:129px;top:1484px;width:700px;font-size:18px;line-height:31px;color:var(--grey)}
.section-title{left:0;width:1200px;text-align:center;font-family:"Poppins",sans-serif;font-weight:600;color:var(--ink)}
.product{position:absolute;top:2025px;width:240px;text-align:center}
.product .ring{position:absolute;left:22px;top:50px;width:196px;height:196px;border-radius:50%;border:6px solid var(--tan)}
.product .ring.featured{border-color:var(--rust)}
.product .bag{position:absolute;left:72px;top:0;width:96px;height:198px;border-radius:6px 6px 3px 3px;background:linear-gradient(180deg,#f6f6f6 0%,#e9e6e2 40%,#d8b990 62%,#3b2418 100%)}
.product h3{position:absolute;top:266px;left:0;width:240px;font-family:"Poppins",sans-serif;font-size:24px;font-weight:500}
.product p{position:absolute;top:310px;left:0;width:240px;font-size:14px;line-height:18px;color:var(--grey)}
.product a{position:absolute;top:361px;left:0;width:240px;font-family:"Poppins",sans-serif;font-style:italic;font-size:15px;color:var(--rust);text-decoration:none}
.connect-title{left:97px;top:2596px;font-family:"Poppins",sans-serif;font-size:40px;font-weight:600;color:var(--white)}
.connect-text{left:99px;top:2660px;width:470px;font-size:16px;line-height:25px;color:var(--white)}
.email{left:91px;top:2774px;width:445px;height:72px;border-radius:40px;background:var(--white);padding-left:26px;display:flex;align-items:center;font-size:15px;color:#6c6662}
.insta-title{left:105px;top:3170px;font-family:"Poppins",sans-serif;font-size:39px;font-weight:500;color:var(--ink)}
.feed{position:absolute;top:3267px;width:241px;height:223px;border-radius:30px}
.divider{left:87px;top:3550px;width:1017px;height:2px;background:#5c5450}
.foot-links a{position:absolute;top:3610px;font-family:"Poppins",sans-serif;font-size:18px;color:var(--ink);text-decoration:none}
.social{position:absolute;top:3673px;width:44px;height:44px;border-radius:50%;border:2px solid var(--ink)}
.copyright{left:94px;top:3750px;font-family:"Poppins",sans-serif;font-size:16px;font-weight:500;color:var(--ink)}
</style>
</head>
<body>

<svg class="backdrop" viewBox="0 0 1200 3859" aria-hidden="true">
  <defs>
    <linearGradient id="aboutFade" x1="0" y1="0" x2="0" y2="1">
      <stop offset="0" stop-color="#3a1812"/>
      <stop offset="0.55" stop-color="#8a6040"/>
      <stop offset="1" stop-color="#d2ad72"/>
    </linearGradient>
    <linearGradient id="connectFade" x1="0" y1="0" x2="0" y2="1">
      <stop offset="0" stop-color="#3a1812"/>
      <stop offset="0.7" stop-color="#5e3222"/>
      <stop offset="1" stop-color="#8a5a3c"/>
    </linearGradient>
  </defs>
  <path d="M0 900 C180 720 330 630 560 590 L1200 560 L1200 1000 C1000 1080 820 1140 620 1200 C400 1260 180 1320 0 1440 Z" fill="url(#aboutFade)"/>
  <path d="M0 0 H1200 V520 C1120 540 1060 590 960 585 C760 575 700 560 560 585 C420 610 320 600 200 560 C110 530 40 515 0 520 Z" fill="var(--espresso)"/>
  <path d="M0 2560 C300 2490 800 2470 1200 2560 V3120 C1080 3060 900 3000 620 2990 C320 2980 120 3010 0 3030 Z" fill="url(#connectFade)"/>
  <path d="M640 3300 C820 3260 1000 3150 1200 3060 V3500 C1080 3420 900 3360 640 3300 Z" fill="var(--tan)"/>
</svg>

<nav class="nav">
  <a class="active" href="#" style="left:114px">Home</a>
  <a href="#" style="left:228px">About Us</a>
  <a href="#" style="left:367px">Our Story</a>
  <a href="#" style="left:746px">Our Products</a>
  <a href="#" style="left:911px">Blog</a>
</nav>
<a class="pill btn-sand" href="#" style="left:975px;top:32px;width:114px;height:40px;font-size:16px">Sign Up</a>
<div class="logo-disc">
  <div class="brand-word" style="font-size:22px">Quiet Falcon<br>Coffee</div>
</div>

<div class="abs hero-kicker">Welcome To</div>
<h1 class="abs hero-title">Quiet Falcon<br>Coffee</h1>
<a class="pill btn-sand" href="#" style="left:114px;top:435px;width:148px;height:40px;font-size:16px">Shop Now</a>
<div class="art" role="img" aria-label="Cartoon rider jumping a horse over a blue and cream fence" style="left:585px;top:127px;width:465px;height:458px;border-radius:40% 45% 20% 30%;background:linear-gradient(160deg,#d8b489 0%,#b08560 55%,#4e7aa8 100%);opacity:.9"></div>

<div class="art" role="img" aria-label="Coffee bag with brand label standing beside a heap of roasted beans" style="left:165px;top:645px;width:330px;height:580px;border-radius:20px 20px 120px 120px;background:linear-gradient(180deg,#f7f7f7 0%,#ece8e3 45%,#e0c39a 70%,#4a2c1e 100%)"></div>
<div class="abs" style="left:166px;top:638px;width:76px;height:76px;border-radius:50%;background:var(--white);border:4px solid #e2a83a"></div>

<div class="abs about-label">ABOUT US</div>
<div class="abs about-sub">Quiet Falcon Coffee</div>
<p class="abs about-text">Sed ut perspiciatis unde omnis iste natus error sit voluptatem accusantium doloremque laudantium, totam rem aperiam, eaque ipsa quae ab illo inventore veritatis et quasi architecto beatae vitae dicta sunt explicabo. Nemo enim ipsam voluptatem quia</p>
<a class="pill btn-dark" href="#" style="left:670px;top:956px;width:150px;height:41px;font-size:16px">Read More</a>

<div class="abs purpose-card"><div class="photo" role="img" aria-label="Soft blurred photo of coffee beans on a table"></div></div>
<div class="art" role="img" aria-label="Cartoon girl in a blue hat riding a grey horse" style="left:825px;top:990px;width:345px;height:555px;border-radius:45% 40% 30% 35%;background:linear-gradient(170deg,#6e96c4 0%,#9ea5ab 45%,#f5e7d2 100%);opacity:.9"></div>
<h2 class="abs purpose-title">Purposes of 4 Different Coffee Bags/Flavors</h2>
<p class="abs purpose-text">Sed ut perspiciatis unde omnis iste natus error sit voluptatem accusantium doloremque laudantium, totam rem aperiam, eaque ipsa quae ab illo inventore veritatis et quasi architecto beatae vitae dicta sunt explicabo. Nemo enim ipsam voluptatem quia voluptas sit aspernatur aut odit aut fugit, sed quia consequuntur magni dolores eos qui ratione voluptatem sequi nesciunt.</p>
<a class="pill btn-dark" href="#" style="left:129px;top:1684px;width:148px;height:41px;font-size:16px">Read More</a>

<h2 class="abs section-title" style="top:1904px;font-size:37px">OUR PRODUCTS</h2>
<div class="product" style="left:114px"><div class="ring"></div><div class="bag" role="img" aria-label="Coffee bag"></div><h3>Coffee</h3><p>Sed ut perspiciatis unde omnis iste natus error sit voluptatem</p><a href="#">View Product ➔</a></div>
<div class="product" style="left:360px"><div class="ring featured"></div><div class="bag" role="img" aria-label="Coffee bag"></div><h3>Coffee</h3><p>Sed ut perspiciatis unde omnis iste natus error sit voluptatem</p><a href="#">View Product ➔</a></div>
<div class="product" style="left:606px"><div class="ring"></div><div class="bag" role="img" aria-label="Coffee bag"></div><h3>Coffee</h3><p>Sed ut perspiciatis unde omnis iste natus error sit voluptatem</p><a href="#">View Product ➔</a></div>
<div class="product" style="left:852px"><div class="ring"></div><div class="bag" role="img" aria-label="Coffee bag"></div><h3>Coffee</h3><p>Sed ut perspiciatis unde omnis iste natus error sit voluptatem</p><a href="#">View Product ➔</a></div>

<h2 class="abs connect-title">Staying Connected</h2>
<p class="abs connect-text">Sed ut perspiciatis unde omnis iste natus error sit voluptatem accusantium doloremque laudantium, totam rem aperiam, eaque ipsa quae</p>
<div class="abs email">Enter your Email</div>
<a class="pill btn-dark" href="#" style="left:94px;top:2876px;width:168px;height:57px;font-size:18px">Send Now</a>
<div class="art" role="img" aria-label="Cartoon cowgirl riding a horse around a barrel above a pile of coffee beans" style="left:682px;top:2487px;width:500px;height:690px;border-radius:40% 45% 35% 40%;background:linear-gradient(170deg,#c9956a 0%,#e7c590 45%,#6b4a3a 100%);opacity:.9"></div>

<h2 class="abs insta-title">Instagram Feed</h2>
<div class="feed" role="img" aria-label="Cup of coffee on a saucer with beans" style="left:99px;background:linear-gradient(135deg,#4a2c1e,#d9cfc6)"></div>
<div class="feed" role="img" aria-label="Ground coffee being scooped" style="left:352px;background:linear-gradient(135deg,#2a1a14,#6b4330)"></div>
<div class="feed" role="img" aria-label="Sack of coffee beans on a wooden table" style="left:607px;background:linear-gradient(135deg,#3a2418,#c49a74)"></div>
<div class="feed" role="img" aria-label="Smiling woman holding a coffee cup" style="left:860px;background:linear-gradient(135deg,#6a4228,#e6d6c8)"></div>

<div class="abs divider"></div>
<nav class="foot-links">
  <a href="#" style="left:96px">Home</a>
  <a href="#" style="left:207px">About Us</a>
  <a href="#" style="left:343px">Our Story</a>
  <a href="#" style="left:482px">Our Products</a>
  <a href="#" style="left:653px">Blog</a>
  <a href="#" style="left:750px">Contact Us</a>
</nav>
<span class="social" style="left:93px" aria-label="Social link"></span>
<span class="social" style="left:144px" aria-label="Social link"></span>
<span class="social" style="left:195px" aria-label="Social link"></span>
<span class="social" style="left:246px" aria-label="Social link"></span>
<span class="social" style="left:297px" aria-label="Social link"></span>
<div class="abs copyright">Copyright © 2025 Company Name . All Rights Reserved.</div>
<div class="abs" style="left:930px;top:3612px;width:84px;height:84px;border-radius:50%;background:var(--tan)"></div>
<div class="abs brand-word" style="left:850px;top:3712px;width:260px;font-size:30px">Quiet Falcon<br>Coffee</div>

</body>
</html>
```